Art for parenting podcast with straight/direct talk...no fluff here! "Plain Answers for Families"

I need an image that will not look fluffy or soft. A no-nonsense look. This is not a 'I love parenting' podcast. It is for frustrated parents who don't know what to do. The name is 'Plain Answers for Families'. The design should, therefore, NOT have hearts and flowers but, instead, look clean and direct. My logo has shades of blue so that would be nice. I have done this work for over 30 years and am well-degreed so would like the design to look stable/established. I have attached my company's logo.

Target Market(s)

Frustrated parents of children - age birth to 20

Industry/Entity Type

Coaching/Counseling for parents

Font styles to use
Serif
Sans Serif

Colors
0054AA
0677BA
7BADD7
CADEEF
E8F1F8

Requirements
Must have
• A look that is clean/bold/direct and professional. Serious.
Nice to have
• If it looks good, my name with my degrees behind my name. MS, MEd. Another thought would be to have a background image of a frustrated parent. Not sure if that would be good or look too busy.
Should not have
• Flowers, fluff, soft appearance, pinks, light colors

```html
<!DOCTYPE html>
<html lang="en">
<head>
<meta charset="UTF-8">
<title>Plain Answers for Families – Podcast Cover</title>
<link href="https://fonts.googleapis.com/css2?family=Oswald:wght@300;600;700&display=swap" rel="stylesheet">
<style>
  :root {
    --navy-deep: #03061a;
    --navy: #0a1f4a;
    --brand-blue: #0054aa;
    --mid-blue: #0677ba;
    --bright-blue: #0a93dc;
    --white: #ffffff;
  }
  html, body {
    margin: 0;
    padding: 0;
    width: 1200px;
    height: 1200px;
    overflow: hidden;
    background: var(--navy-deep);
  }
  .cover {
    position: relative;
    width: 1200px;
    height: 1200px;
    overflow: hidden;
    font-family: "Oswald", "Arial Narrow", sans-serif;
    color: var(--white);
  }
  .cover-photo {
    position: absolute;
    inset: 0;
    background:
      radial-gradient(ellipse 420px 520px at 640px 640px, rgba(0,84,170,0.55), transparent 70%),
      radial-gradient(ellipse 520px 420px at 1100px 300px, rgba(6,119,186,0.95), transparent 75%),
      radial-gradient(ellipse 380px 600px at 1050px 760px, rgba(0,102,180,0.8), transparent 70%),
      linear-gradient(100deg, var(--navy-deep) 0%, #061438 30%, #0a2f6e 60%, var(--brand-blue) 100%);
  }
  .cover-photo::after {
    content: "";
    position: absolute;
    inset: 0;
    background: linear-gradient(180deg, transparent 78%, rgba(3,6,26,0.85) 100%);
  }
  .title {
    position: absolute;
    left: 647px;
    top: 89px;
    transform: translateX(-50%) scaleY(1.15);
    transform-origin: 50% 0;
    margin: 0;
    font-weight: 700;
    font-size: 146px;
    line-height: 141px;
    letter-spacing: -0.5px;
    text-transform: uppercase;
    text-align: center;
    white-space: nowrap;
  }
  .title-line { display: block; }
  .rule {
    position: absolute;
    height: 15px;
  }
  .rule--title {
    left: 165px;
    right: 0;
    top: 419px;
    background: linear-gradient(90deg, rgba(6,119,186,0) 0%, var(--mid-blue) 35%, var(--bright-blue) 100%);
  }
  .rule--footer {
    left: 0;
    right: 0;
    top: 986px;
    height: 16px;
    background: linear-gradient(90deg, var(--bright-blue) 0%, var(--mid-blue) 45%, rgba(6,119,186,0.15) 100%);
  }
  .brand {
    position: absolute;
    left: 780px;
    top: 772px;
    width: 340px;
    text-align: center;
  }
  .brand-dot {
    display: block;
    width: 78px;
    height: 78px;
    margin: 0 auto 18px;
    border-radius: 50%;
    background: var(--white);
  }
  .brand-name {
    margin: 0;
    font-weight: 600;
    font-size: 44px;
    line-height: 48px;
    text-transform: uppercase;
    letter-spacing: 1px;
    color: var(--white);
  }
  .podcast-label {
    position: absolute;
    left: 160px;
    top: 1008px;
    margin: 0;
    font-weight: 300;
    font-size: 144px;
    line-height: 144px;
    letter-spacing: 66px;
    text-transform: uppercase;
    white-space: nowrap;
  }
</style>
</head>
<body>
  <main class="cover">
    <div class="cover-photo" role="img" aria-label="Blue-toned photograph of a frustrated parent holding hands up beside his head, shouting with eyes shut"></div>

    <h1 class="title">
      <span class="title-line">Plain Answers</span>
      <span class="title-line">For Families</span>
    </h1>

    <div class="rule rule--title"></div>

    <div class="brand">
      <span class="brand-dot"></span>
      <p class="brand-name">Steady Ground<br>Parenting</p>
    </div>

    <div class="rule rule--footer"></div>

    <p class="podcast-label">Podcast</p>
  </main>
</body>
</html>
```